Flyer Design Project for our Parenting Psychologists at the Bright Harbour Wellbeing Clinic

At the Bright Harbour Wellbeing Clinic we have expert Parenting Psychologists.

Parenting Psychologists provide practical, step by step assistance to parents who are struggling with their children's behavioural and emotional problems.

We need a DL size brochure that will be appealing to parents. The brochure will be on show in schools, kindergartens and GP clinics.

In terms of style it will be in line with our website and stationery that I will attach.

www.brightharbourwellbeing.com.au
Updates

Hi Everyone,
Thanks for putting forward your proposals, there are a couple there that I am very interested in. I am looking to see if there is a way that I can change my brief to guaranteed as I am definitely going to be using one of the designs for sure.
I have emailed ArtFolkly and as soon as I get an answer I will change it if I can.
If anyone out there already knows the answer please let me know :-)
Thanks,
Marnie.

Hi Again,

I worked it out myself!!

I have now changed this to a committed project.

Kind regards,
Marnie.

Reason: I have 46 designs now and need more time to work out which is best!

Target Market(s)

The target will be educated professional parents motivated to get professional help. And doctors and teachers who will pass on the brochures 2 parents

Industry/Entity Type

Health

Requirements
Must have
• I want one DL size brochure. Back and front.

We need text (below) and our contact details. Our logo.

9362 4158
Suite 1, 2071 Pellbrook Rd, Ferndale Heights 3142

Text:
Parents want the best for their kids. They want kids that are happy, healthy and well behaved.

So why is it so hard? Parents of toddlers, primary schoolers and teenagers alike say that they are frustrated by constant nagging, bribing and yelling, they don't know what to try next. Some parents worry that their children are unhappy. Struggling at school, not making friends or coping with bigger problems.

The good news is that getting your children to behave more co-operatively doesn't need to be difficult or mysterious. We all know that kids don't come with manuals, but there are skills every parent can learn to make parenting easier. In a few sessions with a Parenting Psychologist, you will receive step by step guidance in how to talk to your children in a way that will be much more effective getting them to behave in a respectful and co-operative way around the home and in public. You will learn how to help your child cope with problems they are going through. They can help you reconnect with your kids so you can enjoy being a parent again.

Nice to have
• Themes consistent with our website
and letterhead, business cards. I will attach these.
Should not have
• I don't want it to look too cluttered so if the text I have provided up above looks too crowded then I will edit it.

```html
<!DOCTYPE html>
<html lang="en">
<head>
<meta charset="utf-8">
<title>Bright Harbour Wellbeing Clinic – Parenting Psychologists DL Flyer</title>
<link href="https://fonts.googleapis.com/css2?family=Open+Sans:wght@400;600;700&display=swap" rel="stylesheet">
<style>
  :root {
    --page-bg: #ffffff;
    --panel-cream: #fbf5e5;
    --card-white: #fefefc;
    --brand-green: #3a8d71;
    --olive-text: #a2a46a;
    --mint-text: #92decb;
    --mint-box: #86cdb8;
    --logo-grey: #7d8a88;
    --band-1: #2f9a7e;
    --band-2: #d6efe3;
    --band-3: #5fb98a;
    --band-4: #4d6f66;
    --band-5: #b3e3cd;
    --band-6: #7aa894;
    --band-7: #3fbf9a;
    --band-8: #cfe0b4;
  }
  * { box-sizing: border-box; margin: 0; padding: 0; }
  html, body {
    width: 1200px; height: 1160px; overflow: hidden;
    background: var(--page-bg);
    font-family: "Open Sans", Arial, sans-serif;
  }
  .flyer { position: relative; width: 1200px; height: 1160px; }

  .panel {
    position: absolute; top: 43px; height: 1064px;
    background: var(--panel-cream);
  }
  .panel--front { left: 53px; width: 518px; }
  .panel--back { left: 619px; width: 515px; }

  .colour-band {
    position: absolute; left: 0; width: 100%; height: 48px;
    display: flex;
  }
  .colour-band--top { top: 0; }
  .colour-band--bottom { bottom: 0; height: 36px; }
  .colour-band span { flex: 1; }
  .colour-band span:nth-child(1) { background: var(--band-1); }
  .colour-band span:nth-child(2) { background: var(--band-2); }
  .colour-band span:nth-child(3) { background: var(--band-3); }
  .colour-band span:nth-child(4) { background: var(--band-4); }
  .colour-band span:nth-child(5) { background: var(--band-5); }
  .colour-band span:nth-child(6) { background: var(--band-6); }
  .colour-band span:nth-child(7) { background: var(--band-7); }
  .colour-band span:nth-child(8) { background: var(--band-8); }

  .brand {
    position: absolute; left: 36px; top: 66px;
    display: flex; align-items: center; gap: 18px;
  }
  .brand__dot {
    width: 78px; height: 78px; border-radius: 50%;
    border: 5px solid var(--brand-green); flex: none;
  }
  .brand__name {
    color: var(--logo-grey); font-weight: 400;
    font-size: 19px; letter-spacing: 3px; line-height: 1.3;
    text-transform: uppercase;
  }

  .card {
    position: absolute; background: var(--card-white);
    text-align: center;
  }
  .card--intro { left: 24px; top: 183px; width: 468px; height: 533px; padding: 18px 10px 0; }
  .intro__lead {
    color: var(--brand-green); font-weight: 700;
    font-size: 25px; line-height: 1.38;
  }
  .intro__question {
    color: var(--mint-text); font-weight: 400;
    font-size: 49px; line-height: 1.2; margin: 20px 0 16px;
    white-space: nowrap;
  }
  .intro__body {
    color: var(--olive-text); font-size: 23.5px; line-height: 1.4;
  }

  .photo {
    position: absolute; left: 0; bottom: 0; width: 100%; height: 352px;
    background: linear-gradient(160deg, #4f7a2c 0%, #7fb13e 45%, #a6cf52 75%, #c27a58 100%);
  }

  .card--story { left: 26px; top: 60px; width: 464px; height: 723px; padding: 16px 12px 0; }
  .story__headline {
    color: var(--brand-green); font-weight: 700;
    font-size: 25.5px; line-height: 1.38; margin-bottom: 24px;
  }
  .story__body {
    text-align: left; font-size: 22px; line-height: 1.43;
  }
  .story__body--olive { color: var(--olive-text); margin-bottom: 16px; }
  .story__body--mint { color: var(--mint-text); margin-bottom: 24px; }
  .story__close {
    color: var(--brand-green); font-weight: 700;
    font-size: 25px; line-height: 1.38;
  }

  .contact-box {
    position: absolute; left: 26px; top: 805px; width: 464px; height: 129px;
    background: var(--mint-box); color: #ffffff; text-align: center;
  }
  .contact-box__phone { font-size: 52px; font-weight: 700; line-height: 1; margin-top: 16px; }
  .contact-box__web { font-size: 21px; font-weight: 700; margin-top: 20px; }

  .footer-brand {
    position: absolute; left: 30px; top: 946px;
    display: flex; align-items: center; gap: 10px;
  }
  .footer-brand__dot {
    width: 46px; height: 46px; border-radius: 50%;
    border: 4px solid var(--brand-green); flex: none;
  }
  .footer-brand__name {
    color: var(--logo-grey); font-size: 11px; letter-spacing: 1.6px;
    line-height: 1.35; text-transform: uppercase;
  }
  .address {
    position: absolute; right: 22px; top: 945px;
    color: var(--brand-green); font-size: 19px; line-height: 1.45; text-align: right;
  }
</style>
</head>
<body>
<main class="flyer">

  <section class="panel panel--front">
    <div class="colour-band colour-band--top"><span></span><span></span><span></span><span></span><span></span><span></span><span></span><span></span></div>

    <div class="brand">
      <span class="brand__dot"></span>
      <p class="brand__name">Bright Harbour<br>Wellbeing<br>Clinic</p>
    </div>

    <div class="card card--intro">
      <p class="intro__lead">Parents want the best for their kids. They want kids that are happy, healthy and well behaved.</p>
      <h1 class="intro__question">So Why is it so hard?</h1>
      <p class="intro__body">Parents of toddlers, primary schoolers<br>and teenagers alike say that they are frustrated by constant nagging, bribing and yelling, they don't know what to try next. Some parents worry that their children are unhappy. Struggling at school, not making friends or coping with bigger problems.</p>
    </div>

    <div class="photo" role="img" aria-label="Photo of a mother and her toddler sharing a picnic on green grass in a sunny park"></div>
  </section>

  <section class="panel panel--back">
    <div class="colour-band colour-band--top"><span></span><span></span><span></span><span></span><span></span><span></span><span></span><span></span></div>

    <div class="card card--story">
      <h2 class="story__headline">The good news is that getting<br>your children to behave more co&#8209;operatively doesn't need to be difficult or mysterious.</h2>
      <p class="story__body story__body--olive">We all know that kids don't come with manuals, but there are skills every parent can learn to make parenting easier.</p>
      <p class="story__body story__body--mint">In a few sessions with a Parenting Psychologist, you will receive step by step guidance in how to talk to your children in a way that will be much more effective getting them to behave in a respectful and co&#8209;operative way around the home and in public. You will learn how to help your child cope with problems they are going through.</p>
      <p class="story__close">They can help you reconnect with your kids so you can enjoy being a parent again.</p>
    </div>

    <div class="contact-box">
      <p class="contact-box__phone">P: 9362 4158</p>
      <p class="contact-box__web">www.brightharbourwellbeing.com.au</p>
    </div>

    <div class="footer-brand">
      <span class="footer-brand__dot"></span>
      <p class="footer-brand__name">Bright Harbour<br>Wellbeing<br>Clinic</p>
    </div>
    <p class="address">Suite 1, 2071 Pellbrook Rd<br>Ferndale Heights 3142</p>

    <div class="colour-band colour-band--bottom"><span></span><span></span><span></span><span></span><span></span><span></span><span></span><span></span></div>
  </section>

</main>
</body>
</html>
```